Timeline flyer

Hi, we are an agency, our business is to orienteates student to study abroad in Germany. For that, we enroll them in language schools in Germany and help them to find an accomodation.
Students are always lost we thinked about a timeline to help them figure out what they have to do once in Germany so they don't miss delays.
You can find in the attachement an example that i made in powerpoint but it's really basic and it's only for u so you can understant what the timeline should look like.
We need two time lines.
For the first one (file first timeline)
Title : Procédure pour intégrer le semestre d’hiver dans les universités Allemandes
The first paragraph (up on the left in my proposition) : L’étudiant devra pendant ces mois débuter ses cours d’allemand en Tunisie et les poursuivre en Allemagne après l’obtention du Visa d’étude. L’atteinte du niveau C1 est primordiale pour la bonne réussite du test Kel ou le PLQ.
The second paragraph (below on the left in my proposition) : L’étudiant devra à cette date avoir déjà passer le test KEL ou le PLQ pour pouvoir être à temps pour les inscriptions universitaires. Il faut compter 6 semaines pour le test Kel et 2 à 3 semaines pour obtenir les résultats des tests.
The third one (up on the right in my proposition) : Le dernier délais d’inscription pour pouvoir intégrer une université Allemande pendant la rentrée hivernale (15 Octobre).
The last one (below on the right in my proposition) : Rentrée universitaire
For the second one (file second timeline) :
Title : Procédure pour intégrer le semestre d’été dans les universités Allemandes *
The third one (up on the right in my proposition) : Le dernier délais d’inscription pour pouvoir intégrer une université Allemande pendant la rentrée estivale (15 Avril).
There is also an additional sentence below in the right for this one : * Les spécialités assurées pendant les semestres d’été sont limitées.
You can also find in the attachement our flyers (so you can inspire youself with the color and the design), we want our student to recognize that the flyer is related to our agency so please try to use colors that are matched with the other flyer.
Also, you can find our Logo in the attachement.
Thank you :)
Waiting for your propositions ! :)

```html
<!DOCTYPE html>
<html lang="fr">
<head>
<meta charset="utf-8">
<title>Procédure pour intégrer le semestre d'hiver</title>
<link rel="stylesheet" href="https://fonts.googleapis.com/css2?family=Roboto+Condensed:wght@400;700&display=swap">
<style>
  :root{
    --lime:#8dc63f;
    --leaf:#5f8f25;
    --forest:#3f6a1a;
    --ink:#2e2e2e;
    --muted:#6b6b6b;
    --rule:#c9c9c9;
    --paper:#ffffff;
  }
  *{box-sizing:border-box;margin:0;padding:0}
  html,body{width:1200px;height:850px;overflow:hidden;background:var(--paper)}
  .flyer{position:relative;width:1200px;height:850px;background:var(--paper);
    font-family:"Roboto Condensed",Arial,sans-serif;color:var(--ink);
    border:2px solid var(--rule)}
  .title-band{position:absolute;left:110px;top:14px;right:14px;height:58px;
    background:var(--leaf);display:flex;align-items:center;justify-content:center}
  .title-band::before{content:"";position:absolute;left:-96px;top:0;width:96px;height:58px;background:var(--lime)}
  .title{font-weight:700;font-size:25px;white-space:nowrap;
    color:#fff;text-transform:uppercase;letter-spacing:.3px}
  .brand-name{position:absolute;left:24px;top:440px;width:190px;
    font-weight:700;font-size:32px;line-height:1;color:var(--leaf);white-space:nowrap}
  .timeline{position:absolute;left:0;top:0}
  .date{position:absolute;width:110px;margin-left:-55px;text-align:center;
    font-weight:700;font-size:18px;line-height:1.15;color:var(--muted)}
  .date .month{color:var(--lime)}
  .date.above{top:380px}
  .date.below{top:500px}
  .note{position:absolute;border:2px solid var(--lime);background:var(--paper);
    font-size:15.5px;line-height:1.3;padding:10px 12px;color:var(--ink)}
  .note-language{left:221px;top:176px;width:488px;height:160px}
  .note-deadline{left:742px;top:176px;width:348px;height:122px}
  .note-tests{left:524px;top:540px;width:412px;height:156px}
  .note-start{left:996px;top:596px;width:166px;height:40px;padding:9px 10px;font-weight:700}
  .footer{position:absolute;left:14px;right:14px;bottom:14px;height:52px;border-top:2px solid var(--rule);
    display:flex;align-items:center;gap:28px;padding:0 14px;font-size:14px;font-weight:700;color:var(--forest)}
  .footer .lead{font-size:10px;line-height:1.2;color:var(--ink);width:160px}
  .footer .item{display:flex;align-items:center;gap:7px}
  .footer .chip{width:18px;height:18px;background:var(--lime);border-radius:3px}
  .footer .web{margin-left:auto}
</style>
</head>
<body>
<main class="flyer">
  <header class="title-band">
    <h1 class="title">Procédure pour intégrer le semestre d'hiver dans les universités allemandes</h1>
  </header>

  <div class="brand-name">novaris centre</div>

  <svg class="timeline" width="1200" height="850" viewBox="0 0 1200 850" aria-hidden="true">
    <g stroke="var(--lime)" stroke-width="2" fill="none">
      <line x1="230" y1="478" x2="1160" y2="478" stroke="var(--rule)" stroke-width="4"/>
      <polyline points="300,372 300,356 690,356 690,372"/>
      <line x1="465" y1="336" x2="465" y2="356"/>
      <line x1="885" y1="298" x2="885" y2="470"/>
      <line x1="755" y1="540" x2="755" y2="486"/>
      <line x1="1080" y1="596" x2="1080" y2="556"/>
    </g>
    <g fill="var(--paper)" stroke="var(--lime)" stroke-width="3">
      <circle cx="235" cy="478" r="6"/><circle cx="300" cy="478" r="6"/><circle cx="365" cy="478" r="6"/>
      <circle cx="430" cy="478" r="6"/><circle cx="495" cy="478" r="6"/><circle cx="560" cy="478" r="6"/>
      <circle cx="625" cy="478" r="6"/><circle cx="690" cy="478" r="6"/><circle cx="755" cy="478" r="6"/>
      <circle cx="820" cy="478" r="6"/><circle cx="885" cy="478" r="6"/><circle cx="950" cy="478" r="6"/>
      <circle cx="1015" cy="478" r="6"/><circle cx="1080" cy="478" r="6"/><circle cx="1145" cy="478" r="6"/>
    </g>
  </svg>

  <div class="date below" style="left:235px">2016<br><span class="month">Sep</span></div>
  <div class="date above" style="left:300px"><span class="month">Oct</span><br>2016</div>
  <div class="date below" style="left:365px">2016<br><span class="month">Nov</span></div>
  <div class="date above" style="left:430px"><span class="month">Déc</span><br>2016</div>
  <div class="date below" style="left:495px">2017<br><span class="month">Jan</span></div>
  <div class="date above" style="left:560px"><span class="month">Fév</span><br>2017</div>
  <div class="date below" style="left:625px">2017<br><span class="month">Mars</span></div>
  <div class="date above" style="left:690px"><span class="month">Avr</span><br>2017</div>
  <div class="date below" style="left:755px">2017<br><span class="month">Début Mai</span></div>
  <div class="date above" style="left:820px"><span class="month">Jul</span><br>2017</div>
  <div class="date below" style="left:885px">2017<br><span class="month">15 Juillet</span></div>
  <div class="date above" style="left:950px"><span class="month">Août</span><br>2017</div>
  <div class="date below" style="left:1015px">2017<br><span class="month">Sep</span></div>
  <div class="date above" style="left:1080px;top:360px"><span class="month">15 Octobre</span><br>2017</div>
  <div class="date below" style="left:1145px">2017<br><span class="month">Nov</span></div>

  <p class="note note-language">L'étudiant devra pendant ces mois débuter ses cours d'allemand en Tunisie et les poursuivre en Allemagne après l'obtention du Visa d'étude. L'atteinte du niveau C1 est primordiale pour la bonne réussite du test Kel ou le PLQ.</p>
  <p class="note note-deadline">Le dernier délais d'inscription pour pouvoir intégrer une université Allemande pendant la rentrée hivernale (15 Octobre).</p>
  <p class="note note-tests">L'étudiant devra à cette date avoir déjà passer le test KEL ou le PLQ pour pouvoir être à temps pour les inscriptions universitaires. Il faut compter 6 semaines pour le test Kel et 2 à 3 semaines pour obtenir les résultats des tests.</p>
  <p class="note note-start">Rentrée universitaire</p>

  <footer class="footer">
    <span class="lead">POUR PLUS D'INFORMATIONS<br>CONTACTEZ-NOUS :</span>
    <span class="item"><span class="chip"></span>NOVARIS</span>
    <span class="item">
      <svg width="18" height="18" viewBox="0 0 24 24" aria-hidden="true"><path fill="var(--lime)" d="M6.6 10.8a15 15 0 0 0 6.6 6.6l2.2-2.2c.3-.3.7-.4 1-.2 1.1.4 2.3.6 3.6.6.6 0 1 .4 1 1V20c0 .6-.4 1-1 1A17 17 0 0 1 3 4c0-.6.4-1 1-1h3.5c.6 0 1 .4 1 1 0 1.3.2 2.5.6 3.6.1.3 0 .7-.2 1z"/></svg>
      70 412 508</span>
    <span class="item">FAX : 70 412 509 / GSM : 50 318 776</span>
    <span class="item web">HTTP://NOVARIS.ORG</span>
  </footer>
</main>
</body>
</html>
```